Business Card Design

we are a wellness center offering therapeutic massage modalities and yoga and meditation classes. I would like to see designs that incorporate the colors of my current logo (image uploaded) BUT I would like to change my logo slightly so that the three words wrapping around my image are: massage yoga wellness (in other words, take out skin).

Industry/Entity Type

Massage

Contact Information for Business Card

Lena R. Calloway, BS, CMT, E-RYT, Owner
427 E. Brindle Ave., Suite 3C
Hampton, VA 23581
757-302-5594 (office)
757-861-2047 (cell)
fernleafrestorative.example
fernleafrestorative@mailbox.example

Requirements
Nice to have
• I'd like to have my logo as a watermark on the back side, but if that's not doable, no big deal. Thanks.

```html
<!DOCTYPE html>
<html lang="en">
<head>
<meta charset="utf-8">
<title>Fernleaf Restorative — Business Card</title>
<link href="https://fonts.googleapis.com/css2?family=Open+Sans:wght@400;600;700&display=swap" rel="stylesheet">
<style>
  :root {
    --page: #ecebe8;
    --teal: #a3c6cb;
    --teal-deep: #86b0b7;
    --teal-text: #8fb8be;
    --coral: #e2765a;
    --ink: #333b3d;
    --white: #ffffff;
  }
  * { box-sizing: border-box; margin: 0; padding: 0; }
  html, body {
    width: 1200px; height: 800px; overflow: hidden;
    background: var(--page);
    font-family: "Open Sans", Arial, sans-serif;
  }
  .sheet {
    width: 1200px; height: 800px;
    display: flex; align-items: center; justify-content: center; gap: 40px;
  }
  .card {
    position: relative; width: 540px; height: 309px; overflow: hidden;
    border-radius: 4px;
    box-shadow: 0 6px 18px rgba(0,0,0,.18);
  }

  /* Back side */
  .card--back {
    background: linear-gradient(160deg, var(--teal) 0%, var(--teal-deep) 100%);
  }
  .card--back .watermark {
    position: absolute; right: -70px; bottom: -90px;
    width: 300px; height: 300px; border-radius: 50%;
    background: rgba(255,255,255,.14);
  }
  .card--back .brand {
    position: absolute; left: 44px; top: 96px;
    color: var(--white);
  }
  .brand__name {
    font-size: 40px; font-weight: 600; line-height: 1.1; letter-spacing: .5px;
  }
  .brand__url {
    margin-top: 10px; font-size: 15px; letter-spacing: .5px; color: var(--white);
  }
  .brand__url span { color: var(--coral); }

  /* Front side */
  .card--front { background: var(--white); }
  .card--front svg.wave { position: absolute; inset: 0; }
  .logo {
    position: absolute; right: 30px; top: 26px;
    display: flex; align-items: center; gap: 10px;
  }
  .logo__dot {
    width: 44px; height: 44px; border-radius: 50%; background: var(--teal);
  }
  .logo__name {
    font-size: 24px; font-weight: 600; color: var(--teal-text);
  }
  .person {
    position: absolute; left: 30px; top: 92px;
  }
  .person__name {
    font-size: 19px; font-weight: 700; color: var(--coral);
    text-transform: uppercase; letter-spacing: .5px;
  }
  .person__title {
    margin-top: 4px; font-size: 12px; color: var(--ink);
  }
  .contact {
    position: absolute; right: 22px; top: 140px;
    list-style: none; text-align: right;
  }
  .contact li {
    display: flex; justify-content: flex-end; align-items: center; gap: 8px;
    font-size: 12.5px; color: var(--ink); line-height: 20px;
  }
  .contact .icon {
    width: 16px; height: 16px; border-radius: 50%; background: var(--coral);
    display: flex; align-items: center; justify-content: center;
  }
  .address {
    position: absolute; left: 30px; bottom: 16px;
    font-size: 12.5px; font-weight: 700; color: var(--coral);
    text-transform: uppercase; letter-spacing: .3px;
  }
</style>
</head>
<body>
<main class="sheet">

  <section class="card card--back" aria-label="Card back">
    <div class="watermark"></div>
    <div class="brand">
      <p class="brand__name">Fernleaf<br>Restorative</p>
      <p class="brand__url">www.<span>fernleaf</span>restorative.example</p>
    </div>
  </section>

  <section class="card card--front" aria-label="Card front">
    <svg class="wave" width="540" height="309" viewBox="0 0 540 309">
      <path d="M0,150 C150,165 250,275 540,250 L540,309 L0,309 Z" fill="#e2765a"/>
      <path d="M0,162 C150,180 250,290 540,264 L540,309 L0,309 Z" fill="#a3c6cb"/>
    </svg>

    <div class="logo">
      <span class="logo__dot"></span>
      <span class="logo__name">Fernleaf Restorative</span>
    </div>

    <div class="person">
      <p class="person__name">Lena R. Calloway</p>
      <p class="person__title">BS, CMT, E-RYT, Owner</p>
    </div>

    <ul class="contact">
      <li>555-302-5594
        <span class="icon"><svg width="9" height="9" viewBox="0 0 10 10"><path d="M2 1 L4 3 L3 4 C4 6 4.5 6.5 6 7 L7 6 L9 8 L7.5 9.5 C4 9 1 6 0.5 2.5 Z" fill="#fff"/></svg></span>
      </li>
      <li>555-861-2047
        <span class="icon"><svg width="8" height="10" viewBox="0 0 8 10"><rect x="1" y="0.5" width="6" height="9" rx="1" fill="none" stroke="#fff" stroke-width="1.2"/></svg></span>
      </li>
      <li>fernleafrestorative.example
        <span class="icon"><svg width="10" height="10" viewBox="0 0 10 10" fill="none" stroke="#fff" stroke-width="1"><circle cx="5" cy="5" r="4"/><ellipse cx="5" cy="5" rx="1.8" ry="4"/><path d="M1 5 H9"/></svg></span>
      </li>
      <li>fernleafrestorative@mailbox.example
        <span class="icon"><svg width="10" height="8" viewBox="0 0 10 8" fill="none" stroke="#fff" stroke-width="1"><rect x="0.5" y="0.5" width="9" height="7"/><path d="M0.5 0.5 L5 4.5 L9.5 0.5"/></svg></span>
      </li>
    </ul>

    <p class="address">427 E. Brindle Ave., Suite 3C Marlow Springs, OR 97355</p>
  </section>

</main>
</body>
</html>
```